Business card design Needed for new logo / Construction business, home extensions and new builds

We need a business card design using our new logo files which i will attach to this project :)

We are a small construction business specialising in home extensions, new builds and property development. We are very ambitious and would appreciate professional and elegant designs for our new business card.

Very serious about using the services on BriefNest and recently acquired our new logo from here :)

Please get involved, i will feedback when i can as i am very busy but can respond daily, thanks

Target Market(s)

People that want to build onto their houses, new building developments or adding too their existing property

Industry/Entity Type

Construction

Contact Information for Business Card

Hollin Marsh Construction, Tobias Renwick (Managing Director), Tel 07822200444, email - info@hollin-marsh, www.hollin-marsh.co.uk

Colors

Designer to choose colors to be used in the design.

Requirements
Must have
• I like a deep grey on the back please. A lot of you have provided black from and back, try mixing things up a little. The black looks cool 😎 Thanks

```html
<!DOCTYPE html>
<html lang="en">
<head>
<meta charset="utf-8">
<title>Hollin Marsh Construction – Business Card</title>
<link href="https://fonts.googleapis.com/css2?family=Cinzel:wght@500;600&family=Poppins:wght@400;500&display=swap" rel="stylesheet">
<style>
  :root {
    --stage: #4e4e51;
    --card-back: #2c2c2e;
    --pattern-from: #313133;
    --pattern-to: #262628;
    --card-front: #161616;
    --silver: #d9d9dc;
    --gold: #d9a63a;
    --text: #f1f1f1;
  }
  * { margin: 0; padding: 0; box-sizing: border-box; }
  html, body { width: 1200px; height: 959px; overflow: hidden; }
  body {
    background: var(--stage);
    position: relative;
    font-family: "Poppins", sans-serif;
  }
  .card {
    position: absolute;
    left: 250px;
    width: 700px;
    height: 400px;
    overflow: hidden;
    box-shadow: 0 10px 30px rgba(0,0,0,.45);
  }
  .card--back { top: 53px; background: var(--card-back); }
  .card--front { top: 506px; background: var(--card-front); }

  .back-pattern {
    position: absolute; inset: 0;
    background: linear-gradient(135deg, var(--pattern-from), var(--pattern-to));
  }
  .brand-lockup {
    position: absolute;
    left: 0; right: 0; top: 50%;
    transform: translateY(-50%);
    display: flex; align-items: center; justify-content: center; gap: 16px;
  }
  .brand-square {
    width: 34px; height: 34px;
    background: var(--gold);
  }
  .brand-name {
    font-family: "Cinzel", serif;
    font-weight: 600;
    font-size: 28px;
    letter-spacing: 1px;
    color: var(--gold);
    white-space: nowrap;
  }

  .contact-block {
    position: absolute;
    left: 52px; top: 118px;
  }
  .person-name {
    font-family: "Cinzel", serif;
    font-weight: 600;
    font-size: 36px;
    color: var(--silver);
    letter-spacing: 1px;
    line-height: 1;
    white-space: nowrap;
  }
  .person-role {
    font-size: 20px;
    color: var(--gold);
    margin-top: 6px;
  }
  .company-name {
    font-family: "Cinzel", serif;
    font-weight: 500;
    font-size: 13px;
    color: var(--gold);
    margin-top: 34px;
    letter-spacing: .5px;
  }
  .contact-list { list-style: none; margin-top: 8px; }
  .contact-list li {
    display: flex; align-items: center; gap: 10px;
    font-size: 16px; color: var(--text);
    line-height: 30px;
  }
  .contact-list svg { width: 15px; height: 15px; flex: none; }

  .front-brand {
    position: absolute;
    right: 48px; top: 50%;
    transform: translateY(-50%);
    display: flex; flex-direction: column; align-items: center; gap: 14px;
  }
  .front-brand .brand-square { width: 56px; height: 56px; }
  .front-brand .brand-name { font-size: 24px; }
</style>
</head>
<body>

<section class="card card--back" aria-label="Card back">
  <div class="back-pattern" role="img" aria-label="Subtle tone-on-tone repeated brand pattern on deep grey"></div>
  <div class="brand-lockup">
    <span class="brand-square"></span>
    <span class="brand-name">Hollin Marsh Construction</span>
  </div>
</section>

<section class="card card--front" aria-label="Card front">
  <div class="contact-block">
    <h1 class="person-name">Tobias Renwick</h1>
    <p class="person-role">Managing Director</p>
    <p class="company-name">Hollin Marsh Construction</p>
    <ul class="contact-list">
      <li>
        <svg viewBox="0 0 24 24" aria-hidden="true"><path fill="var(--gold)" d="M6.6 10.8a15 15 0 0 0 6.6 6.6l2.2-2.2c.3-.3.7-.4 1-.2 1.1.4 2.3.6 3.6.6.6 0 1 .4 1 1V20c0 .6-.4 1-1 1A17 17 0 0 1 3 4c0-.6.4-1 1-1h3.5c.6 0 1 .4 1 1 0 1.3.2 2.5.6 3.6.1.3 0 .7-.2 1z"/></svg>
        07822200444
      </li>
      <li>
        <svg viewBox="0 0 24 24" aria-hidden="true"><rect x="2" y="5" width="20" height="14" fill="var(--gold)"/><path d="M2 5l10 8 10-8" fill="none" stroke="var(--card-front)" stroke-width="2"/></svg>
        info@hollin-marsh
      </li>
      <li>
        <svg viewBox="0 0 24 24" aria-hidden="true"><g fill="none" stroke="var(--gold)" stroke-width="2"><circle cx="12" cy="12" r="10"/><ellipse cx="12" cy="12" rx="4" ry="10"/><path d="M2 12h20"/></g></svg>
        www.hollin-marsh.co.uk
      </li>
    </ul>
  </div>
  <div class="front-brand">
    <span class="brand-square"></span>
    <span class="brand-name">Hollin Marsh</span>
  </div>
</section>

</body>
</html>
```